Honigetikett gesucht
Zielgruppe
Es handelt sich um eine kleine Veltara Imkerei unter dem Namen 'Wiesenglanz' im familiären Stiel . Wir sprechen ein breiteres Zielspecktrum an mit dem Fokus auf hochwertige, ökologische aber bodenstände Honig-Produkte.
Aufgabenstellung
Das Design soll für ein Honigettiket dienen und sollte eher minimalistisch aber trotzdem elegant gewählt sein und den Nachhaltigkeitscharakter wiederspiegeln. Das Honigglas mit dem Wabenmusterdeckel ist auch unter folgendem Link zu finden:
https://www.fundo-behalter.de/500g-Honigglas
Abmessungen des Ettiketes:
6,5cm hoch und 20cm breit.
Anbei sind noch beispielhafte Ettiketen angefügt.

```html
<!DOCTYPE html>
<html lang="de">
<head>
<meta charset="utf-8">
<title>Wiesenglanz – Honigetikett Sommerblüte</title>
<link rel="stylesheet" href="https://fonts.googleapis.com/css2?family=Roboto+Condensed:wght@300;400&display=swap">
<style>
  :root {
    --page: #ffffff;
    --paper: #ebe7d8;
    --paper-front: #f2f0e8;
    --ink: #1d1d1b;
    --field: #f1dca0;
  }
  html, body {
    margin: 0;
    padding: 0;
    width: 1200px;
    height: 1133px;
    overflow: hidden;
    background: var(--page);
    font-family: "Roboto Condensed", "Arial Narrow", sans-serif;
    color: var(--ink);
  }
  .label {
    position: absolute;
    left: 0;
    top: 402px;
    width: 1200px;
    height: 329px;
    background: var(--paper);
  }
  .label-front {
    position: absolute;
    left: 284px;
    top: 0;
    width: 632px;
    height: 329px;
    background: var(--paper);
  }
  .label-front-panel {
    position: absolute;
    left: 62px;
    top: 0;
    width: 509px;
    height: 329px;
    background: var(--paper-front);
  }
  .brand-name {
    position: absolute;
    left: 0;
    right: 0;
    top: 112px;
    margin: 0;
    text-align: center;
    font-weight: 400;
    font-size: 60px;
    line-height: 1;
  }
  .product-variety {
    position: absolute;
    left: 0;
    right: 0;
    top: 186px;
    margin: 0;
    text-align: center;
    font-weight: 400;
    font-size: 28px;
    line-height: 1;
    letter-spacing: 14px;
    padding-left: 14px;
  }
  .label-back-left {
    position: absolute;
    left: 26px;
    top: 22px;
    width: 240px;
    font-size: 13px;
    line-height: 16px;
  }
  .label-back-left p { margin: 0 0 16px 0; }
  .net-weight {
    position: absolute;
    left: 26px;
    top: 210px;
    margin: 0;
    font-size: 20px;
  }
  .label-back-right {
    position: absolute;
    left: 934px;
    top: 18px;
    width: 250px;
    font-size: 14px;
    line-height: 18px;
  }
  .field-caption { margin: 0; height: 18px; }
  .field-box {
    width: 243px;
    height: 29px;
    margin: 6px 0 8px 0;
    background: var(--field);
  }
  .storage-note { margin: 0; }
  .storage-note.origin { margin-top: 22px; }
  .storage-note.keep { margin-top: 18px; }
</style>
</head>
<body>
  <section class="label" aria-label="Honigetikett Wiesenglanz Sommerblüte">
    <div class="label-back-left">
      <p>Naturreiner Honig wird nach einiger Zeit fest, er kristallisiert. Durch vorsichtiges erwärmen (max. 40°C) wird er wieder flüssig</p>
      <p>Hergestellt in Deutschland</p>
      <p>Imkerei Wiesenglanz<br>Lindenpfad 3<br>54321 Bienenfeld<br>www.wiesenglanz.de</p>
    </div>
    <p class="net-weight">500g</p>

    <div class="label-front">
      <div class="label-front-panel"></div>
      <h1 class="brand-name">Wiesenglanz</h1>
      <p class="product-variety">SOMMERBLÜTE</p>
    </div>

    <div class="label-back-right">
      <p class="field-caption">Los-No.</p>
      <div class="field-box"></div>
      <p class="field-caption">Mindestens haltbar bis:</p>
      <div class="field-box"></div>
      <p class="field-caption">Datum der Honigernte</p>
      <div class="field-box"></div>
      <p class="field-caption">Standort der Bienenvölker</p>
      <div class="field-box"></div>
      <p class="storage-note origin">Hergestellt in Deutschland</p>
      <p class="storage-note keep">Trocken und vor Wärme geschützt lagern.</p>
    </div>
  </section>
</body>
</html>
```